Business Card Design Project

I am looking for a business card that includes the logo that I am uploading. It is an Interior Design business. This card must include the following (in addition to the logo):
Lena Marbry
Interior Designer - Allied Member, NCDP
4215 Thornwell Lane
Larkfield, MN 55090
612-555-0187
lenajmarbry@quellnet.com
lenamarbryhomes.com

Industry/Entity Type

Business

Requirements
Must have
• This card must include the following (in addition to the logo):
Lena Marbry
4215 Thornwell Lane
Larkfield, MN 55090
612-555-0187
lenajmarbry@quellnet.com
lenamarbryhomes.com

```html
<!DOCTYPE html>
<html lang="en">
<head>
<meta charset="utf-8">
<title>Lena Marbry Interiors – Business Card</title>
<link rel="stylesheet" href="https://fonts.googleapis.com/css2?family=Arimo:wght@400&family=Caveat:wght@400&family=Oswald:wght@300&display=swap">
<style>
  :root {
    --canvas: #ffffff;
    --taupe: #978873;
    --ink-dark: #3b2f22;
    --paper: #ffffff;
    --edge: #cfcfcf;
    --pen: #333333;
  }
  * { margin: 0; padding: 0; box-sizing: border-box; }
  html, body { width: 1200px; height: 900px; overflow: hidden; background: var(--canvas); }
  .canvas { position: relative; width: 1200px; height: 900px; }

  .side-label {
    position: absolute;
    font-family: "Caveat", cursive;
    font-size: 32px;
    color: var(--pen);
    line-height: 1;
  }
  .side-label--front { left: 330px; top: 226px; }
  .side-label--back { left: 832px; top: 226px; }
  .pointer { position: absolute; }
  .pointer--front { left: 404px; top: 244px; }
  .pointer--back { left: 792px; top: 244px; }

  .card {
    position: absolute;
    top: 333px;
    width: 421px;
    height: 242px;
    border-radius: 22px;
    overflow: hidden;
  }
  .card--front { left: 148px; background: var(--taupe); }
  .card--back {
    left: 640px;
    background: var(--paper);
    border: 1.5px solid var(--edge);
  }

  .card__divider {
    position: absolute;
    left: 202px; top: 0;
    width: 6px; height: 100%;
    background: var(--paper);
  }

  .monogram-name {
    position: absolute;
    left: 18px; bottom: 18px;
    font-family: "Oswald", sans-serif;
    font-weight: 300;
    font-size: 30px;
    color: var(--paper);
    line-height: 1;
  }

  .brand-name {
    position: absolute;
    right: 27px; top: 16px;
    font-family: "Oswald", sans-serif;
    font-weight: 300;
    font-size: 24px;
    color: var(--paper);
    letter-spacing: -0.3px;
    white-space: nowrap;
  }

  .contact { font-family: "Arimo", Arial, sans-serif; }
  .contact__name {
    position: absolute;
    left: 311px; top: 68px;
    font-size: 15px;
    color: var(--ink-dark);
  }
  .contact__title {
    position: absolute;
    left: 311px; top: 92px;
    font-size: 7px;
    line-height: 10px;
    color: var(--paper);
  }
  .contact__row { position: absolute; left: 0; width: 100%; font-size: 8.5px; line-height: 12px; }
  .contact__label {
    position: absolute;
    right: 128px;
    text-align: right;
    color: var(--ink-dark);
  }
  .contact__value {
    position: absolute;
    left: 311px;
    color: var(--paper);
    white-space: nowrap;
  }
  .row-address { top: 124px; }
  .row-phone { top: 163px; }
  .row-web { top: 192px; }
  .row-web .contact__value { font-size: 8px; }

  .pattern {
    position: absolute;
    left: 0; top: 2px;
    font-family: "Oswald", sans-serif;
    font-weight: 300;
    font-size: 22px;
    line-height: 26px;
    color: var(--taupe);
    white-space: nowrap;
    letter-spacing: -0.4px;
    word-spacing: 1px;
  }
  .pattern__row { display: block; }
  .pattern__row--shift { margin-left: -44px; }
</style>
</head>
<body>
<main class="canvas">
  <span class="side-label side-label--front">front</span>
  <svg class="pointer pointer--front" width="34" height="44" viewBox="0 0 34 44" aria-hidden="true">
    <path d="M6 2 C20 10 22 24 18 40" fill="none" stroke="var(--pen)" stroke-width="1.3"/>
    <path d="M9 30 L18 40 L28 30" fill="none" stroke="var(--pen)" stroke-width="1.3"/>
  </svg>

  <span class="side-label side-label--back">back</span>
  <svg class="pointer pointer--back" width="34" height="44" viewBox="0 0 34 44" aria-hidden="true">
    <path d="M28 2 C16 10 12 24 16 40" fill="none" stroke="var(--pen)" stroke-width="1.3"/>
    <path d="M4 30 L15 40 L24 30" fill="none" stroke="var(--pen)" stroke-width="1.3"/>
  </svg>

  <section class="card card--front" aria-label="Card front">
    <span class="monogram-name">lena marbry</span>
    <div class="card__divider"></div>
    <h1 class="brand-name">lena marbry interiors</h1>
    <div class="contact">
      <p class="contact__name">Lena Marbry</p>
      <p class="contact__title">Interior Designer<br>allied member, NCDP</p>
      <div class="contact__row row-address">
        <span class="contact__label">address</span>
        <span class="contact__value">4215 Thornwell Lane<br>Larkfield, MN 55090</span>
      </div>
      <div class="contact__row row-phone">
        <span class="contact__label">phone</span>
        <span class="contact__value">612-555-0187</span>
      </div>
      <div class="contact__row row-web">
        <span class="contact__label">mail<br>web</span>
        <span class="contact__value">lenajmarbry@quellnet.com<br>lenamarbryhomes.com</span>
      </div>
    </div>
  </section>

  <section class="card card--back" aria-label="Card back">
    <div class="pattern" aria-hidden="true">
      <span class="pattern__row">lena marbry interiors&nbsp; lena marbry interiors&nbsp; lena marbry interiors</span>
      <span class="pattern__row pattern__row--shift">marbry interiors&nbsp; lena marbry interiors&nbsp; lena marbry interiors&nbsp; lena</span>
      <span class="pattern__row">lena marbry interiors&nbsp; lena marbry interiors&nbsp; lena marbry interiors</span>
      <span class="pattern__row pattern__row--shift">marbry interiors&nbsp; lena marbry interiors&nbsp; lena marbry interiors&nbsp; lena</span>
      <span class="pattern__row">lena marbry interiors&nbsp; lena marbry interiors&nbsp; lena marbry interiors</span>
      <span class="pattern__row pattern__row--shift">marbry interiors&nbsp; lena marbry interiors&nbsp; lena marbry interiors&nbsp; lena</span>
      <span class="pattern__row">lena marbry interiors&nbsp; lena marbry interiors&nbsp; lena marbry interiors</span>
      <span class="pattern__row pattern__row--shift">marbry interiors&nbsp; lena marbry interiors&nbsp; lena marbry interiors&nbsp; lena</span>
      <span class="pattern__row">lena marbry interiors&nbsp; lena marbry interiors&nbsp; lena marbry interiors</span>
    </div>
  </section>
</main>
</body>
</html>
```